Poster needed for hilariously funny interactive FARCE!!

Buried Beneath the Foam is a hilarious interactive murder mystery that takes place in a coffeehouse and bookstore called “Café Pinwheel.” The crazy cast of characters leads the audience through a maze of funny twists and turns. Opportunities for audience and cast interaction reach a peak when the audience is allowed to vote on the ending that they want to hear! There are four possible killers and four possible endings!
Updates

Hello Designers, I am trying to get SKETCHNOOKLY to extend the time of this project. Thanks for your patience. NTP

Target Market(s)

Community and professional Theatres as well as amateur theatre groups

Industry/Entity Type

Cafe

Requirements
Must have
• It must have the title and credit.
• BURIED BENEATH THE FOAM by Ned Parrow
• 'Hilariously funny interactive Murder Mystery'
Nice to have
• The show deals with a coffee shop called 'Cafe Pinwheel' and murder! It is a farce so it should relay that message through the poster.
Should not have
• Photos or images from movies..

```html
<!DOCTYPE html>
<html lang="en">
<head>
<meta charset="utf-8">
<title>Buried Beneath the Foam — Poster</title>
<link rel="stylesheet" href="https://fonts.googleapis.com/css2?family=Bebas+Neue&family=Roboto:wght@300;400;700;900&display=swap">
<style>
  :root {
    --gold: #e2b53a;
    --amber: #c9852b;
    --rust: #a63a22;
    --wine: #6e1f1c;
    --espresso: #2e1410;
    --cream: #efe2c4;
    --ink: #1c0f0a;
    --blood: #c4202a;
  }
  html, body {
    margin: 0;
    padding: 0;
    width: 934px;
    height: 1200px;
    overflow: hidden;
    background: var(--espresso);
  }
  .poster {
    position: relative;
    width: 934px;
    height: 1200px;
    overflow: hidden;
    font-family: "Roboto", Arial, sans-serif;
  }
  .backdrop {
    position: absolute;
    inset: 0;
    background:
      radial-gradient(ellipse 55% 28% at 50% 80%, rgba(170,120,90,0.35), transparent 70%),
      radial-gradient(ellipse 60% 40% at 20% 12%, rgba(240,200,70,0.7), transparent 70%),
      linear-gradient(165deg, var(--gold) 0%, var(--amber) 30%, var(--rust) 55%, var(--wine) 75%, var(--espresso) 100%);
  }
  .tagline {
    position: absolute;
    top: 90px;
    left: 0;
    width: 100%;
    text-align: center;
    font-weight: 400;
    font-size: 18px;
    letter-spacing: 3.4px;
    color: var(--ink);
    margin: 0;
  }
  .title {
    margin: 0;
    font-weight: normal;
  }
  .title span {
    position: absolute;
    left: 0;
    width: 100%;
    text-align: center;
    line-height: 1;
    display: block;
  }
  .title-main {
    top: 196px;
    font-family: "Bebas Neue", Impact, sans-serif;
    font-size: 372px;
    letter-spacing: 4px;
    color: var(--cream);
    text-shadow: 7px 6px 0 var(--ink);
  }
  .title-link {
    top: 588px;
    font-family: "Roboto", Arial, sans-serif;
    font-weight: 300;
    font-size: 94px;
    color: var(--cream);
    -webkit-text-stroke: 2px var(--ink);
    letter-spacing: 1px;
  }
  .title-end {
    top: 696px;
    font-family: "Roboto", Arial, sans-serif;
    font-weight: 900;
    font-size: 110px;
    color: var(--cream);
    letter-spacing: 1px;
  }
  .credit {
    position: absolute;
    top: 966px;
    left: 0;
    width: 100%;
    text-align: center;
    font-weight: 700;
    font-size: 28px;
    color: var(--cream);
    margin: 0;
  }
</style>
</head>
<body>
  <main class="poster">
    <div class="backdrop" role="img" aria-label="Grunge amber-to-wine textured background with red blood splatter and a steaming coffee cup below the title"></div>
    <p class="tagline">HILARIOUSLY FUNNY INTERACTIVE MURDER MYSTERY</p>
    <h1 class="title">
      <span class="title-main">BURIED</span>
      <span class="title-link">BENEATH THE</span>
      <span class="title-end">FOAM</span>
    </h1>
    <p class="credit">BY NED PARROW</p>
  </main>
</body>
</html>
```